Fieldstone Sporting
F.S.S. Sports
Project: Fieldstone Sporting
Fieldstone Sporting - Sports
Creative Brief
Use same font as used in my logo
Use your better judgement
Professional
Weston L. Barrow Jr.
CEO
Harlow Creek, ST
W.barrow17@quillmail.example
www.FSSsports.example
Logo and web address
Concepts
Business card and stationary design. We provide umpires & referees for teams/organizations.

```html
<!DOCTYPE html>
<html lang="en">
<head>
<meta charset="utf-8">
<title>Fieldstone Sporting — Stationery Set</title>
<link href="https://fonts.googleapis.com/css2?family=Arimo:wght@400;700&display=swap" rel="stylesheet">
<style>
  :root {
    --backdrop: #a8a9ac;
    --paper: #ffffff;
    --brand-blue: #4a5392;
    --brand-navy: #1f2a5c;
    --brand-green: #7cbf3a;
    --ink: #3a3a3a;
  }
  html, body {
    margin: 0;
    padding: 0;
    overflow: hidden;
  }
  body {
    width: 1200px;
    height: 626px;
    background: var(--backdrop);
    position: relative;
    font-family: "Arimo", Arial, sans-serif;
    color: var(--ink);
  }
  .sheet {
    position: absolute;
    background: var(--paper);
    box-sizing: border-box;
    overflow: hidden;
  }
  .brand {
    display: flex;
    align-items: center;
    justify-content: center;
    gap: 6px;
    font-weight: 700;
    color: var(--brand-navy);
    white-space: nowrap;
  }
  .brand-dot {
    border-radius: 50%;
    background: var(--brand-green);
    flex: none;
  }
  .band {
    position: absolute;
    left: 0;
    right: 0;
    background: var(--brand-blue);
  }
  .fine {
    position: absolute;
    left: 0;
    right: 0;
    text-align: center;
    white-space: nowrap;
    color: var(--ink);
    line-height: 1;
  }

  /* Business card front */
  .card-front { left: 34px; top: 197px; width: 182px; height: 106px; }
  .card-front .brand { position: absolute; top: 30px; left: 0; right: 0; font-size: 12px; }
  .card-front .brand-dot { width: 9px; height: 9px; }
  .card-front .web { top: 68px; font-size: 5px; }
  .card-front .band { bottom: 0; height: 4px; }

  /* Business card back */
  .card-back { left: 34px; top: 312px; width: 182px; height: 101px; }
  .card-back .name { top: 36px; font-size: 6px; font-weight: 700; }
  .card-back .title { top: 44px; font-size: 4.5px; }
  .card-back .contact-1 { top: 56px; font-size: 4px; }
  .card-back .contact-2 { top: 62px; font-size: 4px; }
  .card-back .web { top: 85px; font-size: 4.5px; }
  .card-back .band { bottom: 0; height: 5px; }

  /* Letterhead */
  .letterhead { left: 233px; top: 10px; width: 425px; height: 590px; }
  .letterhead .band-top { top: 0; height: 14px; }
  .letterhead .brand { position: absolute; top: 60px; left: 0; right: 0; font-size: 19px; }
  .letterhead .brand-dot { width: 13px; height: 13px; }
  .letterhead .web { bottom: 30px; font-size: 6px; font-weight: 700; }
  .letterhead .address { bottom: 20px; font-size: 5.5px; }
  .letterhead .band-bottom { bottom: 0; height: 10px; }

  /* Envelope back */
  .envelope-back { left: 679px; top: 79px; width: 473px; height: 183px; }
  .envelope-back .flap { position: absolute; left: 0; top: 0; width: 473px; height: 183px; }

  /* Envelope front */
  .envelope-front { left: 679px; top: 338px; width: 473px; height: 202px; }
  .envelope-front .band-top { top: 0; height: 12px; }
  .envelope-front .brand { position: absolute; top: 66px; left: 0; right: 0; font-size: 18px; }
  .envelope-front .brand-dot { width: 12px; height: 12px; }
  .envelope-front .web { top: 116px; font-size: 6px; font-weight: 700; }
  .envelope-front .address { top: 125px; font-size: 5.5px; }
  .envelope-front .band-bottom { bottom: 0; height: 12px; }
</style>
</head>
<body>

  <section class="sheet card-front" aria-label="Business card front">
    <div class="brand"><span class="brand-dot"></span>Fieldstone Sporting</div>
    <div class="fine web">www.FSSsports.example</div>
    <div class="band"></div>
  </section>

  <section class="sheet card-back" aria-label="Business card back">
    <div class="fine name">Weston L. Barrow Jr.</div>
    <div class="fine title">CEO</div>
    <div class="fine contact-1">Harlow Creek, ST</div>
    <div class="fine contact-2">W.barrow17@quillmail.example</div>
    <div class="fine web">www.FSSsports.example</div>
    <div class="band"></div>
  </section>

  <section class="sheet letterhead" aria-label="Letterhead">
    <div class="band band-top"></div>
    <div class="brand"><span class="brand-dot"></span>Fieldstone Sporting</div>
    <div class="fine web">www.FSSsports.example</div>
    <div class="fine address">Harlow Creek, ST | Phone: 555-555-0142 Cell: 555-555-0187 Email: W.barrow17@quillmail.example</div>
    <div class="band band-bottom"></div>
  </section>

  <section class="sheet envelope-back" aria-label="Envelope back">
    <svg class="flap" viewBox="0 0 473 183" aria-hidden="true">
      <path d="M0 0 H473 V100 Q473 112 461 112 H400 Q388 112 380 120 Q370 132 352 132 H121 Q103 132 93 120 Q85 112 73 112 H12 Q0 112 0 100 Z" fill="var(--brand-blue)"/>
    </svg>
  </section>

  <section class="sheet envelope-front" aria-label="Envelope front">
    <div class="band band-top"></div>
    <div class="brand"><span class="brand-dot"></span>Fieldstone Sporting</div>
    <div class="fine web">www.FSSsports.example</div>
    <div class="fine address">Harlow Creek, ST | Phone: 555-555-0142 Cell: 555-555-0187 Email: W.barrow17@quillmail.example</div>
    <div class="band band-bottom"></div>
  </section>

</body>
</html>
```